Need a business card design for a residential architect.

You can get a sense of his work at www.tbrelloway.com

Would like a consistent look and feel between business card and website
.

Target Market(s)

Residential homeowners builders

Industry/Entity Type

Residential

Contact Information for Business Card

Dale Brelloway
Principle
Brelloway Architecture
418 Quillfern Lane
Larkmoor, CA 94377

dale@tbrelloway.com

tbrelloway.com
phone: 650-555-0172
Fax: 650-555-0194

Font styles to use
Sans Serif

Requirements
Must have
• Details above
Nice to have
• Would like a consistent look and feel between business card and website
Should not have
• None

```html
<!DOCTYPE html>
<html lang="en">
<head>
<meta charset="utf-8">
<title>Brelloway Architecture — Business Card</title>
<link rel="stylesheet" href="https://fonts.googleapis.com/css2?family=Questrial&display=swap">
<style>
  :root {
    --bg: #e9e9ea;
    --card: #ffffff;
    --ink: #1c1c1c;
    --grey: #7c7c7e;
    --logo: #8e8e90;
    --photo-light: #8fa87a;
    --photo-dark: #5f7452;
  }
  * { margin: 0; padding: 0; box-sizing: border-box; }
  html, body { width: 1200px; height: 720px; overflow: hidden; }
  body {
    background: var(--bg);
    font-family: "Questrial", sans-serif;
    color: var(--ink);
    position: relative;
  }
  .brand-mark {
    position: absolute;
    left: 0; right: 0;
    top: 84px;
    text-align: center;
    color: var(--logo);
    font-size: 38px;
    letter-spacing: 1px;
  }
  .card {
    position: absolute;
    top: 241px;
    width: 420px;
    height: 239px;
    background: var(--card);
    box-shadow: 0 1px 3px rgba(0,0,0,0.12);
  }
  .card--front { left: 147px; }
  .card--back { left: 633px; }

  .card__wordmark {
    position: absolute;
    color: var(--logo);
    font-size: 17px;
    white-space: nowrap;
  }
  .card--front .card__wordmark { left: 20px; top: 32px; }

  .card__tagline {
    position: absolute;
    left: 20px;
    top: 98px;
    font-size: 12px;
    line-height: 19px;
    color: #555;
  }
  .card__photo {
    position: absolute;
    left: 143px;
    top: 19px;
    width: 257px;
    height: 201px;
  }

  .card--back .card__wordmark {
    left: 0; width: 228px;
    top: 98px;
    text-align: center;
  }
  .card__url {
    position: absolute;
    left: 0; width: 228px;
    top: 134px;
    text-align: center;
    font-size: 12px;
  }
  .card__details {
    position: absolute;
    left: 233px;
    top: 57px;
  }
  .card__name { font-size: 19px; line-height: 22px; font-weight: 400; }
  .card__role { font-size: 11.5px; color: var(--grey); margin-top: 1px; }
  .card__contacts { list-style: none; margin-top: 20px; font-size: 11.5px; line-height: 18.5px; }
  .card__contacts .label { color: var(--ink); }
  .card__contacts .value { color: var(--grey); }
  .card__address { margin-top: 13px; font-size: 11.5px; line-height: 19px; color: var(--grey); font-style: normal; }
</style>
</head>
<body>
  <div class="brand-mark">Brelloway Architecture</div>

  <section class="card card--front">
    <div class="card__wordmark">Brelloway Architecture</div>
    <p class="card__tagline">We can help you<br>transform your<br>architectural<br>vision into a reality</p>
    <svg class="card__photo" viewBox="0 0 257 201" role="img" aria-label="Aerial rendering of a modern house with green roof terraces among trees">
      <defs>
        <linearGradient id="photoTone" x1="0" y1="0" x2="1" y2="1">
          <stop offset="0" stop-color="var(--photo-light)"/>
          <stop offset="1" stop-color="var(--photo-dark)"/>
        </linearGradient>
      </defs>
      <path d="M73 0 H257 V201 H0 V58 H73 Z" fill="url(#photoTone)"/>
    </svg>
  </section>

  <section class="card card--back">
    <div class="card__wordmark">Brelloway Architecture</div>
    <div class="card__url">tbrelloway.com</div>
    <div class="card__details">
      <h1 class="card__name">Dale Brelloway</h1>
      <div class="card__role">Principle</div>
      <ul class="card__contacts">
        <li><span class="label">Phone:</span> <span class="value">650.555.0172</span></li>
        <li><span class="label">Fax:</span> <span class="value">650-555-0194</span></li>
        <li><span class="label">Email:</span> <span class="value">dale@tbrelloway.com</span></li>
      </ul>
      <address class="card__address">418 Quillfern Lane Larkmoor,<br>CA 94377</address>
    </div>
  </section>
</body>
</html>
```